Independent International Travel Romantic Comedy Film Poster Design

We need a fun, eye-catching film poster for a romantic comedy shot in San Francisco and throughout the country of Turkey. Very open to cute ideas that grab attention as a small thumbnail.

If your design includes photos and is chosen we would like to take photos of our actors in similar position to replace for your final delivery.

Story: A girl books a trip with her boyfriend, but when he breaks up with her, she is stuck with One-Way Detour tickets in his name. Her friends convince her to find a guy with her ex-boyfriend's name to still go on the trip.

Our film trailer for ideas: https://www.reelhopper.net/watch?v=7Qp4LmN2zRx

Our temp website for ideas: http://www.OneWayDetourFilm.com

Target Market(s)

Young Travelers, Independent Film Lovers, Millennials, 90's RomCom Fans, The Marnie Colter Journals fans

Industry/Entity Type

Travel

Requirements
Must have
• We really want the poster thumbnail to stand out when seen with other independent films on Streamlark.com/ondemand
Nice to have
• Some of our ideas include a "pop-up book map" with characters and iconic landmarks. We like posters for movies like Velvet Errand (pink version), Quietly Tangled, Woman Near the Ferry, Watch Lark Hum, Twelve Rainy Tuesdays, Tide Nine...

```html
<!DOCTYPE html>
<html lang="en">
<head>
<meta charset="utf-8">
<title>One-Way Detour – Film Poster</title>
<link rel="stylesheet" href="https://fonts.googleapis.com/css2?family=Righteous&family=Montserrat:wght@600;700&display=swap">
<style>
  :root {
    --page-bg: #ececec;
    --title-red: #8e1b17;
    --title-shadow: rgba(60, 10, 5, 0.55);
    --band: rgba(255, 236, 200, 0.38);
    --white: #ffffff;
    --photo-green: #9fa56a;
    --photo-yellow: #e9cf8e;
    --photo-tan: #c98d55;
    --photo-sand: #efd6a8;
  }
  * { margin: 0; padding: 0; box-sizing: border-box; }
  html, body {
    width: 1200px;
    height: 746px;
    overflow: hidden;
    background: var(--page-bg);
  }
  .poster {
    position: absolute;
    left: 334px;
    top: 0;
    width: 532px;
    height: 746px;
    overflow: hidden;
    font-family: "Montserrat", Arial, sans-serif;
  }
  .poster__photo {
    position: absolute;
    inset: 0;
    background:
      radial-gradient(ellipse 150px 330px at 390px 330px, rgba(201,141,85,0.95), rgba(201,141,85,0) 100%),
      radial-gradient(ellipse 110px 90px at 385px 510px, rgba(190,110,50,0.9), rgba(190,110,50,0) 100%),
      linear-gradient(180deg, var(--photo-yellow) 0%, var(--photo-green) 45%, #b7a56c 70%, var(--photo-sand) 100%);
  }
  .title-band {
    position: absolute;
    left: 12px;
    top: 158px;
    width: 510px;
    height: 147px;
    background: var(--band);
  }
  .title {
    position: absolute;
    left: 0;
    width: 100%;
    text-align: center;
    font-family: "Righteous", "Arial Black", sans-serif;
    color: var(--title-red);
    text-shadow: 2px 2px 2px var(--title-shadow);
    line-height: 1;
    text-transform: uppercase;
  }
  .title--top { top: 172px; font-size: 56px; letter-spacing: 3px; }
  .title--bottom { top: 232px; font-size: 60px; letter-spacing: 3px; }
  .cast {
    position: absolute;
    left: 34px;
    width: 196px;
    text-align: center;
    color: var(--white);
    font-weight: 600;
    font-size: 18px;
    letter-spacing: 4px;
    line-height: 21px;
    border-bottom: 2px solid var(--white);
    padding-bottom: 4px;
  }
  .cast--first { top: 453px; }
  .cast--second { top: 503px; }
  .synopsis {
    position: absolute;
    left: 20px;
    top: 613px;
    width: 492px;
    text-align: center;
    color: var(--white);
    font-weight: 700;
    font-size: 10.5px;
    letter-spacing: 2.6px;
    line-height: 17.5px;
    text-transform: uppercase;
  }
  .release {
    position: absolute;
    left: 0;
    top: 705px;
    width: 100%;
    text-align: center;
    color: var(--title-red);
    font-weight: 700;
    font-size: 20px;
    letter-spacing: 4px;
  }
</style>
</head>
<body>
  <main class="poster">
    <div class="poster__photo" role="img" aria-label="Soft-focus photo of a woman in a tan coat and hat seen from behind, holding a brown leather suitcase on an autumn tree-lined path"></div>
    <div class="title-band"></div>
    <h1 class="title title--top">One-Way</h1>
    <p class="title title--bottom">Detour</p>
    <p class="cast cast--first">Actor<br>NameSurname</p>
    <p class="cast cast--second">Actor<br>NameSurname</p>
    <p class="synopsis">
      Story: a girl books a trip with her boyfriend, but<br>
      when he breaks up with her, she is stuck<br>
      with One-Way Detour tickets in his name.<br>
      Her friends convince her to find a guy with her<br>
      ex-boyfriend's name to still go on the trip.
    </p>
    <p class="release">JANAURY</p>
  </main>
</body>
</html>
```